Colle Dorata Website

Colle Dorata provides home winemakers and vineyards with ultra-premium frozen wine grapes direct from Italy. Colle Dorata grapes are highly unique, as they are the only wine grapes available worldwide that are 100% Organic and have the prestigious Italian DOCG certification. We have developed a patented process for flash-freezing wine grapes, right after being picked off of our wines in Italy. This ensures unparalleled quality for the most discerning winemakers around the world.
In addition to its expanding line of premium wine grapes, Colle Dorata also imports high-quality winemaking equipment, such as wine vats, pumps, buckets, etc.
We are looking for a professional website designer to redesign www.colledorata-example.com. The redesigned website should have a highly-professional, polished look that conveys our premium product, yet is approachable to our target consumer (target consumer notes below). This website should provide a delightful user experience with the right balance of information and cleanness.
Updates

Requirements
Must have
• 1. Homepage
• 2. About Colle Dorata
• 3. Products Pages
• a. Collection of Wine Grapes
• b. Winemaking Equipment
• 4. Resources (FAQs, videos, other winemaking tools and information)
• 5. Where to Buy
• 6. News and Events
• 7. Contact Us
• Other Requirements and Design Guidance
• • Reference current website copy as a starting point. Feel free to copywrite, but this is not required.
• • Imagery from current site can be used, and new imagery can be added. Be sure that any new stock photography is authentically Italian (our target consumer will know if this is/is not an Italian vineyard/grape image).
• • Feel free to tweak logo slightly, but it must maintain similar look and color scheme.
• • Must include design and coding
• • Must be cross-OS compatible, including mobile
• • Website must be easy to update in the future (updating copy, adding images, etc.)
• • Site must be linked to social media pages (Facebook, Twitter)
• • Brand Objectives
• o Educate consumers about the merits of Colle Dorata products
• o Stir a passion for our products with well placed imagery and copy
• o Compel consumers to learn more about Colle Dorata and act to purchase
• o Create a reason for these loyal consumers to visit Colle Dorata again and again
• o IMPORTANT: Strike the right balance between having an ultra-premium look, yet also providing enough information for consumers. It is important to understand the target consumer (below).
• • Sites for Inspiration
• o
• Deadline:
• 3 Weeks?
• Target Markets:
• 1. Intermediate and advanced home winemakers looking for high-quality wine grapes (and equipment) that is authentically Italian. These consumers typically are affluent but earthy. They often read Cellarcraft Journal – the #1 magazine for home winemaking.
• 2. Small vineyards that are looking to supplement their inventory with high-quality imported wine grapes.
• Look and Feel:
• • Elegant
• • Serious
• • Mondern/Traditional
• • Personable but Professional
• • Gender Neutral
• • Upmarket
Nice to have
• shopping cart

```html
<!DOCTYPE html>
<html lang="en">
<head>
<meta charset="utf-8">
<title>Colle Dorata — Wine Grapes Farmhouse</title>
<link href="https://fonts.googleapis.com/css2?family=Open+Sans:ital,wght@0,300;0,400;0,600;1,400&display=swap" rel="stylesheet">
<style>
:root{
  --wine:#8b0f1f;
  --wine-dark:#6e0a17;
  --orange:#fbab35;
  --header-bg:#fcf6f7;
  --ink:#333333;
  --muted:#444444;
  --grey-panel:#dcdcdc;
  --rule:#d8d8d8;
  --white:#ffffff;
}
*{box-sizing:border-box;margin:0;padding:0}
html,body{width:1200px;height:1191px;overflow:hidden;background:var(--white)}
body{position:relative;font-family:"Open Sans",Arial,sans-serif;color:var(--ink)}
.abs{position:absolute}

.top-strip{left:0;top:0;width:1200px;height:9px;background:var(--wine)}
.site-header{left:0;top:9px;width:1200px;height:104px;background:var(--header-bg)}
.brand{left:139px;top:9px;width:111px;height:104px;background:var(--wine);display:flex;flex-direction:column;align-items:center;justify-content:flex-end;padding-bottom:16px;gap:10px}
.brand-mark{width:26px;height:26px;border:2px solid var(--white);border-radius:50%}
.brand-name{color:var(--white);font-size:9.5px;font-weight:600;letter-spacing:.2px}
.lang{left:957px;top:9px;width:101px;height:33px;background:var(--wine);color:var(--white);font-size:12px;display:flex;align-items:center;justify-content:center}
.nav-accent{left:322px;top:44px;width:30px;height:26px;border-radius:50%;background:linear-gradient(135deg,#c9d86a,#7c9a2e)}
.main-nav a{position:absolute;top:80px;transform:translateX(-50%);font-size:16px;color:var(--muted);text-decoration:none;font-weight:400;white-space:nowrap}

.hero{left:1px;top:113px;width:1199px;height:403px;background:linear-gradient(180deg,#f7a024 0%,#f6c33a 28%,#c7a642 44%,#4f6a25 62%,#3b4a1f 80%,#4b4425 100%)}
.hero-arrow{top:300px;width:62px;height:61px;background:rgba(139,15,31,.45);display:flex;align-items:center;justify-content:center}
.hero-arrow svg{width:18px;height:26px}
.hero-title{left:138px;top:415px;color:var(--white);font-weight:300;line-height:1}
.hero-title .t1{display:block;font-size:36px}
.hero-title .t2{display:block;font-size:28px;margin-top:6px}
.hero-dots{left:602px;top:466px;display:flex;gap:15px}
.hero-dots span{width:19px;height:19px;border-radius:50%;background:var(--wine-dark)}

.promo{left:746px;top:459px;width:313px;height:194px;background:var(--wine);color:var(--white);padding:22px 0 0 30px}
.promo h2{font-weight:400;font-size:25px;line-height:1.05;width:175px;position:relative;z-index:2}
.promo p{font-style:italic;font-size:10px;line-height:1.3;width:150px;margin-top:10px;position:relative;z-index:2}
.btn{background:var(--orange);color:var(--white);font-size:14px;display:flex;align-items:center;justify-content:center;text-decoration:none}
.promo .btn{position:absolute;left:30px;top:140px;width:108px;height:33px}
.promo-visual{left:958px;top:462px;width:136px;height:172px;border-radius:45% 50% 40% 55%;background:radial-gradient(circle at 55% 55%,#d9e27d,#a9bb46 55%,#4d8a2c 100%)}

.search{left:746px;top:657px;width:313px;height:84px;background:var(--wine)}
.search-input{position:absolute;left:30px;top:26px;width:177px;height:33px;background:var(--white);border:0}
.search .btn{position:absolute;left:211px;top:26px;width:78px;height:33px;font-size:13px}

.news{left:746px;top:745px;width:313px;height:209px}
.news-head{height:57px;background:var(--wine);color:var(--white);font-size:21px;font-weight:400;padding:16px 0 0 30px}
.news-body{height:152px;background:var(--grey-panel);padding:16px 28px 0 28px;font-size:12.5px}
.news-date{color:var(--ink)}
.news-place{color:var(--wine);font-style:italic;margin-top:1px}
.news-text{margin-top:10px;line-height:1.35;color:var(--muted);font-size:12px}
.news .btn{position:absolute;left:29px;top:175px;width:78px;height:34px}

.section-title{left:137px;font-size:22px;font-weight:400;color:var(--ink);letter-spacing:.1px}
.intro{left:139px;top:595px;width:575px;font-size:11.6px;line-height:17px;color:var(--muted)}

.feature{left:139px;width:511px;height:139px;background:var(--wine);color:var(--white)}
.feature .copy{position:absolute;font-size:12px;line-height:17px}
.feature .btn{position:absolute;width:78px;height:34px}
.feature-visual{position:absolute;top:0;height:139px}

.footer-nav{left:0;top:1078px;width:1200px;height:47px;border-top:1px solid var(--rule);border-bottom:1px solid var(--rule)}
.footer-nav ul{list-style:none;display:flex;position:absolute;left:140px;top:13px;font-size:13.5px;letter-spacing:.5px;color:var(--muted)}
.footer-nav li{white-space:nowrap}
.footer-nav .sep{margin:0 30px}
.copyright{left:139px;top:1151px;font-size:12.5px;color:var(--muted)}
.social{left:859px;top:1140px;display:flex;gap:7.5px}
.social span{width:30px;height:30px;border-radius:50%;border:2px solid #222}
.social span:first-child{border-color:var(--wine)}
</style>
</head>
<body>
  <div class="abs top-strip"></div>
  <header class="abs site-header"></header>

  <div class="abs brand">
    <span class="brand-mark"></span>
    <span class="brand-name">COLLE DORATA</span>
  </div>
  <div class="abs lang">Italy | English</div>

  <div class="abs nav-accent" role="img" aria-label="Small bunch of green grapes"></div>
  <nav class="main-nav">
    <a style="left:338px" href="#">About Us</a>
    <a style="left:460px" href="#">Order</a>
    <a style="left:590px" href="#">The Collection</a>
    <a style="left:736px;top:79px" href="#">News/Events</a>
    <a style="left:867px" href="#">FAQ</a>
    <a style="left:1002px" href="#">Contact</a>
  </nav>

  <section class="abs hero" role="img" aria-label="Tuscan vineyard rows under a golden sky with a line of trees on the hill"></section>
  <a class="abs hero-arrow" style="left:140px" href="#" aria-label="Previous slide">
    <svg viewBox="0 0 18 26"><polyline points="15,2 3,13 15,24" fill="none" stroke="#fff" stroke-width="2"/></svg>
  </a>
  <a class="abs hero-arrow" style="left:997px" href="#" aria-label="Next slide">
    <svg viewBox="0 0 18 26"><polyline points="3,2 15,13 3,24" fill="none" stroke="#fff" stroke-width="2"/></svg>
  </a>
  <h1 class="abs hero-title"><span class="t1">COLLE DORATA</span><span class="t2">WINE GRAPES FARMHOUSE</span></h1>
  <div class="abs hero-dots"><span></span><span></span><span></span><span></span></div>

  <aside class="abs promo">
    <h2>Frozen Italian Grapes</h2>
    <p>Invest in your cellar and elevate your winemaking with the Colle Dorata Collection at Prairie Cellar Supply</p>
    <a class="btn" href="#">ORDER NOW</a>
  </aside>
  <div class="abs promo-visual" role="img" aria-label="Bunch of green wine grapes with vine leaves"></div>

  <form class="abs search">
    <input class="search-input" type="text" aria-label="Search">
    <a class="btn" href="#">SEARCH</a>
  </form>

  <aside class="abs news">
    <div class="news-head">NEWS &amp; EVENTS</div>
    <div class="news-body">
      <div class="news-date">AUGUST 20, 2011</div>
      <div class="news-place">Philadelphia, PA</div>
      <p class="news-text">Colle Dorata’s renowned enologist discussed the Colle Dorata 2011 harvest at Ridgeline Homebrew.</p>
    </div>
    <a class="btn" href="#">more</a>
  </aside>

  <h2 class="abs section-title" style="top:548px">REDEFINING THE ART OF WINEMAKING</h2>
  <p class="abs intro">With over 15 years of home and commercial winemaking experience, Colle Dorata elevates your winemaking experience with premium Italian grape musts from the heart of Tuscany. Colle Dorata brings the Tuscan vineyard to your doorstep, with 5 select varietals that are 100% Organic and DOCG Certified.</p>

  <h2 class="abs section-title" style="top:691px">WELCOME TO COLLE DORATA</h2>
  <div class="abs feature" style="top:722px">
    <p class="copy" style="left:27px;top:31px;width:226px">Colle Dorata’s premium grape musts elevate the art of winemaking for home winemakers and accomplished vineyards alike.</p>
    <a class="btn" href="#" style="left:182px;top:105px">more</a>
    <div class="feature-visual" style="left:259px;width:252px;background:linear-gradient(180deg,#b9c3cc 0%,#8c9a7c 40%,#6f8a3e 70%,#7f9a3a 100%)" role="img" aria-label="Tuscan hillside villa among cypress trees and vineyards"></div>
  </div>

  <h2 class="abs section-title" style="top:888px">COLLE DORATA COLLECTION</h2>
  <div class="abs feature" style="top:919px">
    <div class="feature-visual" style="left:1px;width:251px;background:linear-gradient(180deg,#5a3a5e 0%,#8a4a5a 45%,#c0583a 75%,#1d1010 100%)" role="img" aria-label="Silhouette of a vine at sunset"></div>
    <p class="copy" style="left:274px;top:30px;width:222px">Each Colle Dorata varietal is nurtured to its fullest flavor and color, then picked by our commercially-certified enologist.</p>
    <a class="btn" href="#" style="left:433px;top:105px">more</a>
  </div>

  <nav class="abs footer-nav">
    <ul>
      <li>HOME</li><li class="sep">.</li>
      <li>ORDER</li><li class="sep">.</li>
      <li>ABOUT US</li><li class="sep">.</li>
      <li>THE COLLECTION</li><li class="sep">.</li>
      <li>NEWS/EVENTS</li><li class="sep">.</li>
      <li>FAQ</li><li class="sep">.</li>
      <li>CONTACT</li>
    </ul>
  </nav>

  <p class="abs copyright">©2013 Colle Dorata</p>
  <div class="abs social" aria-label="Social media links">
    <span></span><span></span><span></span><span></span><span></span>
  </div>
</body>
</html>
```